Small Business Directory Site Requires a Professional Responsive Web Design

Small Business Directory and Coupon Site - we require a complete website design for a brand new responsive & mobile friendly website. We already have a coder who will professional code our website in Magento.

All PSD pages need to be professionally designed then uploaded into a sharedrive (i.e. like dropbox). Additionally, as I cannot pre-empt everything, please note that we may require a little more assistance once the files have been transferred (for example, in www.brindlestack.com if you hover your mouse on the search box you will see a pop up box. We want one of these too and I think that means there may be extra design work here)

We have some draft page sketches have been created (there are some minor changes we want to the sketches provided though); however, we require an excellent designer to add the creative touches to it to make it look professionally created. All artwork/font must be legal.

-------------------------
We like the look of the www.brindlestack.com and www. quorvanet.com

For the headers, please consider a font similar to RNS camellia. We likes this style, but it is too thin for the headers...so we need a variation like this one. For the copy/general text font, something basic that marries well with the headers.

---------------------

Please be sure to also read the brief we wrote for the coder as this will help with better understanding our design requirements.

In total I believe we have about 50 pages. This includes all the little pages and most of the pop up boxes (but not the little help key boxes). For example, pages include...

1. Login (this is where customers log in and can edit, manage their profiles. This means that there are backend membership pages)
2. Mini Services (same look and feel as the business coupons)
3. Resource Centre
4. Join (this is where customers learn about the packages available to submit a directory listing, if they ‘buy’ a package (i.e. free, $25 or $150 package) then they can create their own directory listing)
5. Search the directory (customer can view all the categories and also search the directory)
6. Create a directory listing (this is where customers learn about the packages available to submit a directory listing, if they ‘buy’ a package (i.e. free, $25 or $150 package) then they can create their own directory listing)
7. Quote finder (also know as Get a Quote)
8. Coupons (customer go to the business coupon page and can view all current coupons/submit a coupon)
9. Submit a coupon (form)
10.Advertise with us (form)
11. Join the forum
12.Submit an article or video (form)
13. Affiliates (listing of affiliates we currently have)
14. Become an affiliate (form)
15. Case studies (customer can view the case studies we have in the resource centre)
16. Help Guides (customer can view the help guides we have in the resource centre)
17. About Us
18 .Contact Us (form)
19. Terms & Condition
20. Privacy Policy
21. Supporting City Councils
22. Site Map
23. Forgot password / login details
24. Homepage
25. If we hover over a few areas (i.e. search box, location field) it pops up with more information.
etc etc etc. . . there are more pages.

Please see our dropbox link for the draft mock up pages that I have created so far.

https://www.filmorrow.com/sh/kq82pl4vmd7wtz/QZtrXnBeLopVacd3Ju7fGhWkS

We are in a rush! We'd like to get the majority of the artwork completed by the end of the month. Minor fixes/tweaks can occur thereafter.

Target Market(s)

Small Businesses (employees 0 - 50) located throughout Australia

Industry/Entity Type

Business

Font styles to use
Sans Serif

Requirements
Must have
• Professional. Artwork must be legal (cannot be cut and paste or taken off other websites, must be legally purchased and used).Must look contemporary, fresh, modern.

Absolutely must be a responsive site!
Nice to have
• original work, original photos, original art.

like modern, fresh photos that demonstrate innovation, growth, small business, Australian scenery, stability, goals/passion.
Should not have
• cut and paste graphics, illegal graphics, not purchased graphics.

```html
<!DOCTYPE html>
<html lang="en">
<head>
<meta charset="utf-8">
<title>Bizlane Hub — Small Business Directory</title>
<link rel="stylesheet" href="https://fonts.googleapis.com/css2?family=Roboto:wght@300;400;500&display=swap">
<style>
:root{
  --black:#000;
  --ink:#333;
  --muted:#555;
  --orange:#f7931e;
  --orange-text:#f39423;
  --white:#fff;
  --band:#ececec;
  --footer-bar:#1e1e1e;
  --dark-btn:#2a2a2a;
}
*{box-sizing:border-box;margin:0;padding:0}
html,body{width:1094px;height:1200px;overflow:hidden}
body{position:relative;font-family:'Roboto',Arial,sans-serif;background:var(--white);color:var(--ink)}
.abs{position:absolute}

.site-header{left:0;top:0;width:1094px;height:96px;background:var(--black)}
.brand{left:160px;top:36px;display:flex;align-items:center;gap:8px;color:var(--white);font-size:20px;font-weight:400;letter-spacing:.5px}
.brand-mark{width:18px;height:18px;background:var(--orange)}
.main-nav{left:453px;top:43px;display:flex;gap:16px;font-size:13px;color:var(--white)}

.hero{left:0;top:96px;width:1094px;height:432px;background:linear-gradient(180deg,#8c8782 0%,#c9c3bc 45%,#d8d2ca 70%,#a09486 100%)}
.hero-title{left:160px;top:194px;font-size:41px;font-weight:500;color:var(--white)}
.hero-sub{left:160px;top:243px;font-size:22px;font-weight:300;color:var(--white);letter-spacing:.5px}
.search-bar{left:159px;top:287px;width:386px;height:66px;background:var(--orange)}
.search-field{top:15px;height:35px;background:var(--white);font-size:9.5px;color:#444;padding:13px 10px}
.search-what{left:13px;width:173px}
.search-near{left:195px;top:29px;font-size:10px;color:#5a3a00}
.search-where{left:225px;width:109px}
.search-icon{left:342px;top:18px}
.join-btn{left:558px;top:288px;width:118px;height:64px;background:linear-gradient(#3a3a3a,#151515);color:var(--white);font-size:13.5px;display:flex;align-items:center;justify-content:center;border-radius:2px}

.ad-box{left:711px;top:163px;width:228px;height:271px;background:#ccc;border:2px solid #222;text-align:center}
.ad-box h3{font-weight:400;font-size:14px;color:#222;margin-top:12px;line-height:16px}
.ad-inner{left:20px;top:55px;width:181px;height:197px;background:var(--white)}
.ad-card{left:13px;top:12px;width:156px;height:176px;border:2px solid #ddd;border-radius:4px;font-size:12px;color:#222}
.ad-card p{line-height:17px}
.ad-price{left:-4px;top:91px;width:160px;height:28px;background:#626262;color:var(--white);font-size:16px;line-height:28px}
.ad-cta{left:20px;top:131px;width:115px;height:30px;background:var(--orange);color:var(--white);font-size:12.5px;line-height:30px}
.ad-arrow{top:110px;width:40px;height:34px;background:#3a3a3a;display:flex;align-items:center;justify-content:center}
.hero-dots{left:1057px;top:319px;display:flex;flex-direction:column;gap:11px}
.hero-dots span{width:8px;height:8px;border-radius:50%;background:var(--white)}
.hero-dots span:first-child{background:var(--orange)}

.section-title{left:0;top:557px;width:1094px;text-align:center;font-size:17.5px;color:var(--orange-text)}
.feature{top:612px;width:222px}
.feature h4{font-size:14px;font-weight:400;color:#444;height:40px}
.feature-media{width:221px;height:128px}
.feature p{font-size:9.8px;line-height:15px;color:#333;margin-top:17px;text-align:justify}
.partner-name{height:128px;display:flex;align-items:center;gap:10px;font-size:30px;font-weight:500;color:#1d3a6e;padding-left:14px}
.partner-name i{width:28px;height:28px;border-radius:50%;background:#1f8bd0}

.logo-band{left:0;top:876px;width:1094px;height:85px;background:var(--band)}
.sponsor{top:30px;font-size:24px;font-weight:500;color:#222}

.site-footer{left:0;top:961px;width:1094px;height:177px;background:var(--black);color:var(--white)}
.foot-col{top:21px}
.foot-col h5{font-size:14px;font-weight:500;color:var(--orange-text);margin-bottom:13px}
.foot-col li{list-style:none;font-size:11px;line-height:20.3px}
.social{display:flex;gap:13px}
.social span{width:33px;height:33px;border-radius:50%;border:2px solid #ddd}
.copyright{left:0;top:1138px;width:1094px;height:62px;background:var(--footer-bar);color:#ddd;font-size:11px;text-align:center;line-height:62px}
</style>
</head>
<body>
<header class="site-header abs">
  <div class="brand abs"><span class="brand-mark"></span>Bizlane Hub</div>
  <nav class="main-nav abs"><span>Login</span><span>Join</span><span>Coupounts</span><span>Mini Services</span><span>Get a Quote</span><span>Advertise</span><span>Resoure Centre</span></nav>
</header>

<section class="hero abs" role="img" aria-label="Bright living room with a white sofa, table lamps and a potted plant">
  <h1 class="hero-title abs">It's a Brand New Day</h1>
  <p class="hero-sub abs">DO MORE OF WHAT YOU LOVE</p>
  <div class="search-bar abs">
    <div class="search-field search-what abs">What are vou looking for?</div>
    <span class="search-near abs">near</span>
    <div class="search-field search-where abs">Where?</div>
    <svg class="search-icon abs" width="30" height="30" viewBox="0 0 30 30"><circle cx="12" cy="12" r="9" fill="none" stroke="#fff" stroke-width="3"/><line x1="18.5" y1="18.5" x2="27" y2="27" stroke="#fff" stroke-width="4" stroke-linecap="round"/></svg>
  </div>
  <div class="join-btn abs">Join Us Today</div>
  <div class="ad-box abs">
    <h3>Advertise<br>your business</h3>
    <div class="ad-inner abs">
      <div class="ad-card abs">
        <p style="margin-top:14px">It's simple<br>and affordable</p>
        <p style="margin-top:14px">Starting from just</p>
        <div class="ad-price abs">$2 per day.</div>
        <div class="ad-cta abs">GET STARTED</div>
      </div>
    </div>
    <div class="ad-arrow abs" style="left:-8px"><svg width="12" height="16"><polyline points="9,2 3,8 9,14" fill="none" stroke="#fff" stroke-width="3"/></svg></div>
    <div class="ad-arrow abs" style="left:190px"><svg width="12" height="16"><polyline points="3,2 9,8 3,14" fill="none" stroke="#fff" stroke-width="3"/></svg></div>
  </div>
  <div class="hero-dots abs"><span></span><span></span><span></span><span></span><span></span></div>
</section>

<h2 class="section-title abs">GET REAL SUPPORT FROM OUR COMMUNITY</h2>

<article class="feature abs" style="left:159px">
  <h4>How Did You Sort Your Business?</h4>
  <div class="feature-media" role="img" aria-label="Calculator and pen resting on a financial chart" style="background:linear-gradient(135deg,#c9d6e6,#e9eef5 60%,#b4c3d6)"></div>
  <p>Learn from Mara Lindqvist, a real small business owner. How she started her business and what are the most valuable resources for her right now.</p>
</article>

<article class="feature abs" style="left:435px">
  <h4>Why Go with Bizlane Hub?</h4>
  <div class="feature-media" role="img" aria-label="Video: designer's desk with floor plans and colour swatches" style="background:linear-gradient(135deg,#dfe3e8,#f4f4f4 55%,#cfd6de);position:relative">
    <svg class="abs" style="left:94px;top:48px" width="34" height="34"><circle cx="17" cy="17" r="16" fill="#333" opacity=".75"/><polygon points="13,10 25,17 13,24" fill="#fff"/></svg>
  </div>
  <p>What small business owner can't relate to the ongoing task of attracting new customers? Struggling with cash flow? Or how about not And that's where we come in.</p>
</article>

<article class="feature abs" style="left:712px">
  <h4>Become an Affiliate</h4>
  <div class="partner-name"><i></i>Harbor Mutual</div>
  <p>If you have a network of small businesses, let us help to create additional value for your members and make money for your network. Talk to us today about how we can help.</p>
</article>

<section class="logo-band abs">
  <span class="sponsor abs" style="left:204px">Ferrowind</span>
  <span class="sponsor abs" style="left:494px">Plexora</span>
  <span class="sponsor abs" style="left:790px">Zentric</span>
</section>

<footer class="site-footer abs">
  <div class="foot-col abs" style="left:162px"><h5>Site Directry</h5><ul><li>Search the&nbsp; Directry</li><li>Create a&nbsp;&nbsp; Directry listing</li><li>Quote Finder</li><li>Submit a Coupon</li><li>Advertise With Us</li></ul></div>
  <div class="foot-col abs" style="left:310px"><h5>Resourose</h5><ul><li>Join the forum</li><li>submit an article or video</li><li>Affect</li><li>Become an affect</li><li>case studies</li></ul></div>
  <div class="foot-col abs" style="left:467px"><h5>Popular Categoires</h5><ul><li>Search the&nbsp; Directry</li><li>Create a&nbsp;&nbsp; Directry listing</li><li>Quote Finder</li><li>Submit a Coupon</li><li>Advertise With Us</li></ul></div>
  <div class="foot-col abs" style="left:625px"><h5>About</h5><ul><li>About us</li><li>Contact us</li><li>Terms &amp; Conditions</li><li>Supporting by cound</li><li>site map</li></ul></div>
  <div class="foot-col abs" style="left:765px"><h5>Follow us</h5>
    <div class="social"><span style="background:#3b5998" aria-label="Friendloop"></span><span style="background:#1da1f2" aria-label="Chirpline"></span><span style="background:#d34836" aria-label="Circlewave"></span><span style="background:#1a84bc" aria-label="Workgrid"></span></div>
  </div>
</footer>
<div class="copyright abs">Copyright © 2014 All rights reserved.</div>
</body>
</html>
```